Kelvane Plumbing Business cards

Company is Kelvane Plumbing.
name Dashel Morrowby, I am a plumber, drainer, gasfitter and roofer
Mobile: 0431 906 154
Email address: info@kelvaneplumbing.example (check out my website for some ideas)
Website: www.kelvaneplumbing.example
ABN: 82 916 203 471
LIC: 604517K

I am reliable all round plumber. I am a 24 hour emergency service. Kelvane Plumbing is a professional plumbing service in the Illawarra, South Coast, Southern Sydney and Southern Highland regions of NSW. We offer a 24 hour emergency service for piece of mind to our customers. Call us now to see how we can help you. Kelvane Plumbing approaches every job with attention to detail and excellent customer service. With our superior workmanship you can be confident that the job will be done right the first time around. You can rest assured with results that are guaranteed to last.

Target Market(s)

the general public

Contact Information for Business Card

look up website for some ideas something with similar colours to logo and new modern and to catch the eye.

Colors
fdfdfd
ffffff
000000
7f7f7f
aaaaaa
33a6d7
0492cd

Requirements
Must have
• all contact details
• company- Kelvane Plumbing
• name- Dashel Morrowby
• number mobile- 0431 906 154
• Email address- info@kelvaneplumbing.example
• Website- www.kelvaneplumbing.example
• ABN- 82 916 203 471
• LIC- 604517K

```html
<!DOCTYPE html>
<html lang="en">
<head>
<meta charset="utf-8">
<title>Kelvane Plumbing – Business Cards</title>
<link rel="stylesheet" href="https://fonts.googleapis.com/css2?family=Montserrat:wght@400;500;700&display=swap">
<style>
  :root {
    --blue: #0492cd;
    --blue-light: #33a6d7;
    --grey: #7f7f7f;
    --grey-light: #aaaaaa;
    --white: #ffffff;
    --off-white: #fdfdfd;
    --navy: #11141c;
    --stage: #e9eaec;
    --ink: #555555;
  }
  * { margin: 0; padding: 0; box-sizing: border-box; }
  html, body {
    width: 1200px; height: 880px; overflow: hidden;
    background: var(--stage);
    font-family: "Montserrat", Arial, sans-serif;
  }
  .canvas { position: relative; width: 1200px; height: 880px; }

  .card {
    position: absolute;
    width: 700px; height: 390px;
    border-radius: 26px;
    overflow: hidden;
    box-shadow: 0 8px 24px rgba(0,0,0,.18);
  }

  /* Back */
  .card-back { left: 60px; top: 40px; background: var(--navy); }
  .back-brand {
    position: absolute; inset: 0;
    display: flex; align-items: center; justify-content: center; gap: 14px;
  }
  .brand-dot { width: 22px; height: 22px; border-radius: 50%; background: var(--grey); }
  .back-brand .brand-name {
    font-weight: 700; font-size: 30px; color: var(--blue); letter-spacing: .5px;
  }

  /* Front */
  .card-front { left: 440px; top: 450px; background: var(--white); }
  .front-shapes { position: absolute; inset: 0; }
  .front-brand {
    position: absolute; right: 40px; top: 78px; width: 290px;
    display: flex; flex-direction: column; align-items: center; gap: 14px;
  }
  .front-brand .brand-ring {
    width: 120px; height: 120px; border-radius: 50%;
    border: 12px solid var(--grey);
  }
  .front-brand .brand-name {
    font-weight: 700; font-size: 30px; color: var(--blue); text-align: center; line-height: 1.1;
  }
  .company {
    position: absolute; left: 40px; top: 92px;
    font-weight: 700; font-size: 34px; color: var(--blue);
  }
  .company .company-rest { color: var(--grey); }
  .person { position: absolute; left: 40px; top: 168px; }
  .person-name { font-weight: 700; font-size: 24px; color: var(--blue); }
  .person-role { font-size: 15px; color: var(--grey); margin-top: 2px; }
  .contacts { position: absolute; left: 40px; top: 232px; list-style: none; }
  .contacts li {
    display: flex; align-items: center; gap: 10px;
    font-size: 15px; color: var(--ink); height: 25px;
  }
  .contacts .icon { width: 19px; height: 19px; flex: none; }
  .contacts .web-domain { color: var(--blue); }
  .reg-band {
    position: absolute; left: 40px; bottom: 12px;
    font-size: 15px; font-weight: 500; color: var(--white); letter-spacing: .4px;
  }
</style>
</head>
<body>
<main class="canvas">

  <section class="card card-back" aria-label="Card back">
    <div class="back-brand">
      <span class="brand-dot"></span>
      <span class="brand-name">Kelvane Plumbing</span>
    </div>
  </section>

  <section class="card card-front" aria-label="Card front">
    <svg class="front-shapes" width="700" height="390" viewBox="0 0 700 390" aria-hidden="true">
      <polygon points="600,0 700,0 700,390 560,390" fill="var(--grey)" opacity=".9"/>
      <polygon points="0,345 700,280 700,390 0,390" fill="var(--grey)"/>
      <polygon points="0,351 700,288 700,390 0,390" fill="var(--blue)"/>
    </svg>

    <div class="front-brand">
      <span class="brand-ring"></span>
      <span class="brand-name">Kelvane Plumbing</span>
    </div>

    <h1 class="company">Kelvane <span class="company-rest">Plumbing</span></h1>

    <div class="person">
      <p class="person-name">Dashel Morrowby</p>
      <p class="person-role">Plumber | Drainer | Gasfitter | Roofer</p>
    </div>

    <ul class="contacts">
      <li>
        <svg class="icon" viewBox="0 0 20 20" aria-hidden="true"><circle cx="10" cy="10" r="10" fill="var(--blue)"/><rect x="7" y="4.5" width="6" height="11" rx="1.2" fill="none" stroke="#fff" stroke-width="1.4"/><circle cx="10" cy="13.4" r=".8" fill="#fff"/></svg>
        <span>0431 906 154</span>
      </li>
      <li>
        <svg class="icon" viewBox="0 0 20 20" aria-hidden="true"><circle cx="10" cy="10" r="10" fill="var(--blue)"/><rect x="5" y="6.5" width="10" height="7" fill="none" stroke="#fff" stroke-width="1.3"/><polyline points="5,6.5 10,10.8 15,6.5" fill="none" stroke="#fff" stroke-width="1.3"/></svg>
        <span>info@kelvaneplumbing.example</span>
      </li>
      <li>
        <svg class="icon" viewBox="0 0 20 20" aria-hidden="true"><circle cx="10" cy="10" r="10" fill="var(--blue)"/><circle cx="10" cy="10" r="5.5" fill="none" stroke="#fff" stroke-width="1.2"/><ellipse cx="10" cy="10" rx="2.4" ry="5.5" fill="none" stroke="#fff" stroke-width="1.1"/><line x1="4.5" y1="10" x2="15.5" y2="10" stroke="#fff" stroke-width="1.1"/></svg>
        <span>www.<span class="web-domain">kelvaneplumbing</span>.example</span>
      </li>
    </ul>

    <p class="reg-band">ABN- 82 916 203 471 | LIC- 604517K</p>
  </section>

</main>
</body>
</html>
```